Tindle Crest Funds Bus card and Logo

I need a logo design and Bus card design. The fund focuses on evaluating and investing in minerals (sub-surface rights) and real estate.

Tindle crest refers to a book of knowledge that each plebe gets when entering the DL Verrant Academy (my alma mater)

Target Market(s)

Investors and financial advisors

Contact Information for Business Card

Simple - perhaps a logo with a theme on book of knowledge

Logo Text

Ex Scientia Imperium

Font styles to use
Serif
Sans Serif

Colors

Designer to choose colors to be used in the design.

Requirements
Must have
• memorable logo that is relatively simple

```html
<!DOCTYPE html>
<html lang="en">
<head>
<meta charset="utf-8">
<title>Tindle Crest Funds – Business Card</title>
<link href="https://fonts.googleapis.com/css2?family=Cinzel:wght@600&family=Arimo:wght@400;700&display=swap" rel="stylesheet">
<style>
  :root {
    --backdrop: #2d2d2f;
    --card: #ffffff;
    --navy: #0f5aa0;
    --brand-blue: #1d5ea8;
    --mark-blue: #2aa3dd;
    --violet: #6c6ab0;
    --white: #ffffff;
  }
  * { box-sizing: border-box; margin: 0; padding: 0; }
  html, body { width: 1200px; height: 880px; overflow: hidden; }
  body {
    background: var(--backdrop);
    display: flex;
    align-items: center;
    justify-content: center;
    gap: 28px;
    font-family: "Arimo", Arial, sans-serif;
  }
  .card {
    position: relative;
    width: 560px;
    height: 320px;
    background: var(--card);
    border-radius: 18px;
    overflow: hidden;
  }
  .wordmark {
    position: absolute;
    display: flex;
    flex-direction: column;
    align-items: center;
    color: var(--brand-blue);
    font-family: "Cinzel", "Times New Roman", serif;
    font-weight: 600;
  }
  .wordmark__mark {
    width: 58px; height: 58px; border-radius: 50%;
    background: var(--mark-blue);
    margin-bottom: 12px;
  }
  .wordmark__name { font-size: 34px; letter-spacing: 1px; line-height: 1; }
  .wordmark__sub {
    display: flex; align-items: center; gap: 10px;
    font-size: 14px; letter-spacing: 4px; margin-top: 6px;
  }
  .wordmark__sub::before, .wordmark__sub::after {
    content: ""; width: 40px; height: 1.5px; background: var(--brand-blue);
  }
  .card--front .wordmark { left: 0; right: 0; top: 82px; }
  .card--back .wordmark { left: 40px; top: 62px; }
  .card--back .wordmark__mark { width: 50px; height: 50px; margin-bottom: 10px; }
  .card--back .wordmark__name { font-size: 28px; }
  .card--back .wordmark__sub { font-size: 12px; }
  .card__waves { position: absolute; inset: 0; width: 100%; height: 100%; }
  .holder {
    position: absolute; right: 60px; top: 30px; text-align: right;
  }
  .holder__name { color: var(--navy); font-weight: 700; font-size: 19px; }
  .holder__role { color: var(--violet); font-size: 13px; margin-top: 2px; }
  .contact {
    position: absolute; right: 22px; top: 152px;
    list-style: none; color: var(--white); font-size: 12.5px; text-align: right;
  }
  .contact li { display: flex; align-items: center; justify-content: flex-end; gap: 7px; height: 19px; }
  .contact .icon { width: 14px; height: 14px; flex: none; }
  .contact .spacer { width: 14px; }
</style>
</head>
<body>
  <section class="card card--front">
    <div class="wordmark">
      <span class="wordmark__mark" role="img" aria-label="Tindle Crest Funds emblem"></span>
      <span class="wordmark__name">TINDLE CREST</span>
      <span class="wordmark__sub">FUNDS LLC</span>
    </div>
  </section>

  <section class="card card--back">
    <svg class="card__waves" viewBox="0 0 560 320" preserveAspectRatio="none" aria-hidden="true">
      <path fill="var(--violet)" d="M0,270 C120,262 205,245 248,192 C272,160 284,132 290,112 C292,150 278,192 257,222 C215,280 130,290 0,292 Z"/>
      <path fill="var(--navy)" d="M110,304 C215,288 255,244 290,186 C330,132 390,106 500,100 C410,114 360,142 326,190 C290,244 240,290 110,304 Z"/>
      <path fill="var(--navy)" d="M0,320 L0,302 C150,298 240,264 290,204 C335,150 385,126 560,122 L560,320 Z"/>
    </svg>

    <div class="wordmark">
      <span class="wordmark__mark" role="img" aria-label="Tindle Crest Funds emblem"></span>
      <span class="wordmark__name">TINDLE CREST</span>
      <span class="wordmark__sub">FUNDS LLC</span>
    </div>

    <div class="holder">
      <p class="holder__name">Marcus Hale</p>
      <p class="holder__role">Manager</p>
    </div>

    <ul class="contact">
      <li>PO BOX 418, Ashford Lane<span class="spacer"></span></li>
      <li>2nd street Ashford<span class="spacer"></span></li>
      <li>555.010.2468
        <svg class="icon" viewBox="0 0 16 16"><circle cx="8" cy="8" r="7" fill="none" stroke="#fff" stroke-width="1.4"/><path d="M5.5 4.5 L7 6 L6 7.2 C6.6 8.5 7.5 9.4 8.8 10 L10 9 L11.5 10.5 L10.5 11.6 C7.6 11.2 4.8 8.4 4.4 5.5 Z" fill="#fff"/></svg>
      </li>
      <li>info@tindlecrest.com
        <svg class="icon" viewBox="0 0 16 16"><circle cx="8" cy="8" r="7" fill="none" stroke="#fff" stroke-width="1.4"/><rect x="4.3" y="5.3" width="7.4" height="5.4" fill="#fff"/><path d="M4.3 5.3 L8 8.4 L11.7 5.3" fill="none" stroke="var(--navy)" stroke-width="0.9"/></svg>
      </li>
      <li>www.tindlecrest.com
        <svg class="icon" viewBox="0 0 16 16"><circle cx="8" cy="8" r="7" fill="none" stroke="#fff" stroke-width="1.4"/><circle cx="8" cy="8" r="4" fill="none" stroke="#fff" stroke-width="0.9"/><path d="M4 8 H12 M8 4 V12" stroke="#fff" stroke-width="0.9"/></svg>
      </li>
    </ul>
  </section>
</body>
</html>
```